professional business card

Professional business card with logo on one side, and underneath logo list:
- power
-data
-fibre optic
-isolar

On other side:
Marcus Webb
Owner
MOB 0432 958 720
marcus@vorn.com.au
www.vornelectrical.com.au

Please edit logo to just leave VORN

```html
<!DOCTYPE html>
<html lang="en">
<head>
<meta charset="UTF-8">
<title>Vorn Electrical – Business Card</title>
<link href="https://fonts.googleapis.com/css2?family=Roboto:wght@300;400;500;700&display=swap" rel="stylesheet">
<style>
  :root {
    --backdrop: #3a3a3c;
    --card: #262628;
    --teal: #0f8f98;
    --teal-deep: #0b6e75;
    --silver: #8d8f93;
    --text-light: #e6e6e6;
    --text-muted: #a9abaf;
  }
  * { margin: 0; padding: 0; box-sizing: border-box; }
  html, body {
    width: 799px;
    height: 1200px;
    overflow: hidden;
    background: var(--backdrop);
    font-family: "Roboto", sans-serif;
  }
  .sheet {
    width: 799px;
    height: 1200px;
    display: flex;
    flex-direction: column;
    align-items: center;
    justify-content: space-around;
    padding: 60px 0;
  }
  .card {
    position: relative;
    width: 660px;
    height: 377px;
    background: var(--card);
    border-radius: 4px;
    box-shadow: 0 18px 40px rgba(0,0,0,0.45);
    overflow: hidden;
  }

  /* Front */
  .card-front {
    display: flex;
    flex-direction: column;
    align-items: center;
    justify-content: center;
  }
  .brand-front {
    font-size: 96px;
    font-weight: 700;
    letter-spacing: 6px;
    color: var(--silver);
    line-height: 1;
  }
  .services {
    margin-top: 26px;
    font-size: 15px;
    font-weight: 400;
    letter-spacing: 1.5px;
    color: var(--text-muted);
  }
  .services .divider {
    color: var(--teal);
    margin: 0 8px;
  }
  .website-front {
    margin-top: 44px;
    font-size: 15px;
    font-weight: 300;
    color: var(--text-muted);
    letter-spacing: 0.5px;
  }

  /* Back */
  .card-back { padding: 48px 0 0 54px; }
  .back-info { position: relative; z-index: 1; width: 300px; }
  .brand-back {
    font-size: 64px;
    font-weight: 700;
    letter-spacing: 4px;
    color: var(--teal);
    line-height: 1;
  }
  .person { margin-top: 42px; }
  .person-name {
    font-size: 24px;
    font-weight: 400;
    color: var(--teal);
  }
  .person-role {
    margin-top: 4px;
    font-size: 13px;
    font-weight: 400;
    color: var(--text-light);
  }
  .contact-list {
    list-style: none;
    margin-top: 26px;
  }
  .contact-item {
    display: flex;
    align-items: center;
    gap: 12px;
    font-size: 15px;
    font-weight: 400;
    color: var(--text-light);
    margin-bottom: 8px;
  }
  .contact-icon { width: 14px; height: 14px; flex: none; }

  .brand-decoration {
    position: absolute;
    top: 0;
    right: 0;
    width: 290px;
    height: 100%;
    background: linear-gradient(120deg, var(--teal-deep) 0%, var(--teal) 55%, var(--teal-deep) 100%);
  }
</style>
</head>
<body>
  <main class="sheet">
    <section class="card card-front">
      <div class="brand-front">VORN</div>
      <p class="services">
        POWER<span class="divider">|</span>DATA<span class="divider">|</span>FIBRE OPTIC<span class="divider">|</span>ISOLAR
      </p>
      <p class="website-front">www.vornelectrical.com.au</p>
    </section>

    <section class="card card-back">
      <div class="brand-decoration" role="img" aria-label="Large teal brand stripe decoration"></div>
      <div class="back-info">
        <div class="brand-back">VORN</div>
        <div class="person">
          <p class="person-name">Marcus Webb</p>
          <p class="person-role">Owner</p>
        </div>
        <ul class="contact-list">
          <li class="contact-item">
            <svg class="contact-icon" viewBox="0 0 14 14" aria-hidden="true">
              <path d="M3 1h2.5l1 3-1.5 1a8 8 0 0 0 4 4l1-1.5 3 1V11a2 2 0 0 1-2 2A11 11 0 0 1 1 3a2 2 0 0 1 2-2z" fill="var(--teal)"/>
            </svg>
            0432 958 720
          </li>
          <li class="contact-item">
            <svg class="contact-icon" viewBox="0 0 14 14" aria-hidden="true">
              <rect x="1" y="3" width="12" height="8.5" rx="1" fill="var(--teal)"/>
              <path d="M1.5 3.5 7 8l5.5-4.5" fill="none" stroke="var(--card)" stroke-width="1.2"/>
            </svg>
            marcus@vorn.com.au
          </li>
          <li class="contact-item">
            <svg class="contact-icon" viewBox="0 0 14 14" aria-hidden="true">
              <circle cx="7" cy="7" r="6" fill="var(--teal)"/>
              <path d="M1 7h12M7 1c-2.5 3-2.5 9 0 12M7 1c2.5 3 2.5 9 0 12" fill="none" stroke="var(--card)" stroke-width="0.9"/>
            </svg>
            vornelectrical.com.au
          </li>
        </ul>
      </div>
    </section>
  </main>
</body>
</html>
```